Website Update for Global Company - Solar Technology - GreenTech

We recently released our first version of our website kelvaro.com. However despite a longer process of developing the page, it is still missing the elements of a brilliant website. (Currently it looks dead and boring) We are having problems integrating our logo and want to create a more catching site. The task involves an updated and without changing most of main elements in the existing page. (Unless you can do it even better) The blue color needs to be kept but can be changed within the blue-spectrum. The logo text (KELVARO) must be better integrated in the site, however the main logo could be used in elements like we have tried with the background. The surface of the logo could be changed to 3D or metallic, or any other theme that would make the site more complete.
It would be good if some elements of the site could be used on business cards and invoices to keep the company identity.
Kelvaro is a new development company specialized in green energy and sustainable development. We do design, engineering, manufacturing, sourcing and other processes related to product development – both as consultants and for own products.
Keep the look of the site as professional as possible, and with a cooperate-looking style.

Link to existing page: www.kelvaro.com

Brief Update : After reviewing the designs we would like all new and current designers to make more bold designs that stands out from the rest. We do not like the standard layout that looks like any other cooperate homepage. We want a very unique and very lively page - with faded images and effects when hoovering like seen on our existing page. Try make all elements blend together, and use faded background images instead of just white color - or something else.

Make the site unique !

Industry/Entity Type

Solar Energy

Contact Information for Business Card

Owner/Founder/CEO : Tobias Haldrup Jessen
Company name: Kelvaro ApS
Email: tobias.haldrup@kelvaro-mail.dk
Phone: +45 61 87 34 09
Slogan Sustainable Development
Address: Hyldegade 18, 2
DK-5700 Svendborg, Denmark

Number of Pages Required

3 page

Font styles to use
Serif
Sans Serif

Colors
0555a3
85acd3
cedeed
3176b5
cee9f5
85cae6
0293ce
86cfc6
33b8a4

```html
<!DOCTYPE html>
<html lang="en">
<head>
<meta charset="utf-8">
<title>Kelvaro – Sustainable Solutions</title>
<link href="https://fonts.googleapis.com/css2?family=Open+Sans:wght@300;400;600;700&display=swap" rel="stylesheet">
<style>
:root{
  --navy:#0555a3;
  --blue:#3176b5;
  --cyan:#0293ce;
  --sky:#85cae6;
  --pale:#cedeed;
  --ice:#cee9f5;
  --ink:#1d3550;
  --page:#e9eef3;
  --footer:#0a1724;
  --white:#ffffff;
}
*{box-sizing:border-box;margin:0;padding:0}
html,body{width:1200px;height:2744px;overflow:hidden}
body{font-family:"Open Sans",Arial,sans-serif;background:linear-gradient(180deg,#e4ebf2 0%,#eef2f6 50%,#e2e9f0 100%);color:var(--ink);position:relative}
.site-header{position:absolute;top:0;left:0;width:1200px;height:100px;background:var(--white);display:flex;align-items:center;justify-content:space-between;padding:0 88px}
.brand{display:flex;align-items:center;gap:12px}
.brand-mark{width:34px;height:34px;background:var(--navy)}
.brand-name{font-weight:700;font-size:34px;letter-spacing:2px;color:var(--navy);line-height:1}
.brand-tag{font-size:10px;letter-spacing:3px;color:var(--blue);margin-top:4px}
.main-nav{display:flex;gap:46px}
.main-nav a{font-size:14px;font-weight:600;letter-spacing:1px;color:var(--ink);text-decoration:none}
.hero{position:absolute;top:100px;left:0;width:1200px;height:348px;background:
  linear-gradient(180deg,rgba(255,255,255,0) 70%,rgba(233,238,243,.9) 100%),
  radial-gradient(ellipse at 75% 20%,rgba(255,255,255,.55),rgba(255,255,255,0) 45%),
  linear-gradient(160deg,#0a4f95 0%,#1e7cc6 40%,#8cc7ea 75%,#d6ecf7 100%)}
.hero-copy{position:absolute;left:88px;top:130px;color:var(--white)}
.hero-title{font-weight:300;font-size:40px;letter-spacing:3px;line-height:48px}
.hero-title b{font-weight:600}
.hero-sub{font-size:13px;margin-top:14px;opacity:.9}
.hero-btn{display:inline-block;margin-top:26px;margin-left:40px;background:var(--navy);color:var(--white);font-size:12px;font-weight:700;letter-spacing:2px;padding:10px 30px}
.tiles{position:absolute;top:544px;left:88px;width:1024px;display:grid;grid-template-columns:repeat(3,324px);grid-auto-rows:280px;gap:28px 26px}
.tile{position:relative;overflow:hidden;background:var(--pale);text-decoration:none}
.tile.photo::after{content:"";position:absolute;inset:0;background:
  radial-gradient(ellipse at 70% 30%,rgba(255,255,255,.22),rgba(255,255,255,0) 55%),
  linear-gradient(180deg,rgba(0,0,0,0) 55%,rgba(6,30,60,.45) 100%)}
.tile .label{position:absolute;z-index:1;left:24px;bottom:22px;right:50px;color:var(--white);font-size:17px;font-weight:600;letter-spacing:1px;text-transform:uppercase;line-height:22px}
.tile .chev{position:absolute;z-index:1;right:22px;bottom:22px;width:14px;height:22px}
.wide{grid-column:span 2}
.tall{grid-row:span 2}
.news{background:var(--white);padding:18px 24px}
.news h2{font-size:16px;font-weight:700;color:var(--cyan);letter-spacing:1px;border-bottom:2px solid var(--cyan);padding-bottom:7px;line-height:22px}
.news-item{display:flex;align-items:center;gap:14px;margin-top:11px;height:43px;background:#eef1f4}
.news-item:first-of-type{margin-top:13px}
.news-date{width:48px;height:43px;background:#c9d3dc;color:var(--white);font-size:10px;font-weight:700;text-align:center;padding-top:8px;line-height:13px;flex:none}
.news-item.active .news-date{background:var(--cyan)}
.news-title{font-size:12px;color:#5a6b7c}
.statement{background:var(--cyan);display:flex}
.statement .dots{width:110px;flex:none;background:radial-gradient(ellipse at 0 50%,#ffffff 0%,#bfe6f6 40%,rgba(2,147,206,0) 75%)}
.statement p{padding:26px 20px 26px 4px;color:var(--white);font-size:21px;font-weight:700;line-height:32px;text-transform:uppercase;letter-spacing:1px}
.site-footer{position:absolute;top:2470px;left:0;width:1200px;height:274px;background:var(--footer);color:#9fb2c4}
.foot-col{position:absolute;top:48px}
.foot-col h3{font-size:11px;font-weight:700;color:var(--cyan);letter-spacing:1px;margin-bottom:10px}
.foot-col li{list-style:none;font-size:10px;line-height:17px;letter-spacing:.5px}
.foot-brand{position:absolute;left:800px;top:56px;display:flex;align-items:center;gap:12px}
.foot-brand .brand-mark{background:var(--white)}
.foot-brand .brand-name{color:var(--white)}
.foot-phone{position:absolute;left:800px;top:128px;font-size:18px;color:var(--cyan);letter-spacing:1px}
.social{position:absolute;left:990px;top:132px;display:flex;gap:12px}
.social span{width:16px;height:16px;border-radius:50%;background:#9fb2c4}
.copyright{position:absolute;left:800px;top:166px;font-size:10px}
</style>
</head>
<body>
<header class="site-header">
  <div class="brand">
    <div class="brand-mark"></div>
    <div>
      <div class="brand-name">KELVARO</div>
      <div class="brand-tag">SUSTAINABLE SOLUTIONS</div>
    </div>
  </div>
  <nav class="main-nav">
    <a href="#">WORK</a><a href="#">EXPERTISE</a><a href="#">APPROACH</a><a href="#">CLIENTS</a><a href="#">ABOUT</a><a href="#">CONTACT</a>
  </nav>
</header>

<section class="hero" role="img" aria-label="Solar panel field under a bright blue sky">
  <div class="hero-copy">
    <h1 class="hero-title">DESIGN <b>+</b> ENGINEERING<br>SOURCING <b>+</b> MANUFACTURING</h1>
    <p class="hero-sub">We are a development company specialised in green energy and sustainable development.</p>
    <span class="hero-btn">ABOUT US</span>
  </div>
</section>

<main class="tiles">
  <div class="tile news">
    <h2>IN THE NEWS</h2>
    <div class="news-item active"><div class="news-date">05<br>AUG</div><span class="news-title">Launch of website</span></div>
    <div class="news-item"><div class="news-date">01<br>JUL</div><span class="news-title">First project finished</span></div>
    <div class="news-item"><div class="news-date">20<br>APR</div><span class="news-title">Establishment of Kelvaro ApS</span></div>
    <div class="news-item"><div class="news-date">02<br>MAR</div><span class="news-title">Establishment of Kelvaro ApS</span></div>
  </div>
  <a class="tile wide photo" role="img" aria-label="Hand touching glowing blue gear icons" style="background:radial-gradient(ellipse at 62% 40%,#5ec0f0 0%,#1676c4 30%,#0a2c5a 75%)">
    <span class="label">Featured innovation</span>
    <svg class="chev" viewBox="0 0 14 22"><path d="M2 2l9 9-9 9" fill="none" stroke="#fff" stroke-width="3"/></svg>
  </a>

  <a class="tile wide photo" role="img" aria-label="Designer sketching product drawings at a desk" style="background:radial-gradient(ellipse at 40% 30%,#a89686 0%,#6e5a4e 35%,#241d1c 90%)">
    <span class="label">Our work</span>
    <svg class="chev" viewBox="0 0 14 22"><path d="M2 2l9 9-9 9" fill="none" stroke="#fff" stroke-width="3"/></svg>
  </a>
  <a class="tile photo" role="img" aria-label="Rows of solar panels in a green landscape" style="background:linear-gradient(180deg,#c9e0f0 0%,#8fb7d8 35%,#3f6e9c 60%,#4e6a44 100%)">
    <span class="label">Project videos</span>
    <svg class="chev" viewBox="0 0 14 22"><path d="M1 2l12 9-12 9z" fill="#fff"/></svg>
  </a>

  <div class="tile statement">
    <div class="dots" role="img" aria-label="Halftone dot pattern"></div>
    <p>Kelvaro is made up of talented + diverse individuals</p>
  </div>
  <a class="tile photo" role="img" aria-label="Glowing light bulb on a dark background" style="background:radial-gradient(circle at 50% 38%,#e6f3fb,#5a9fd4 25%,#1a4f86 50%,#0b1c30 85%)">
    <span class="label">Focused innovation</span>
    <svg class="chev" viewBox="0 0 14 22"><path d="M2 2l9 9-9 9" fill="none" stroke="#fff" stroke-width="3"/></svg>
  </a>
  <a class="tile photo" role="img" aria-label="Pencil sketch of a sports car design" style="background:linear-gradient(135deg,#f4f4f4,#d2d2d2 55%,#8f8f8f)">
    <span class="label">Industrial design</span>
    <svg class="chev" viewBox="0 0 14 22"><path d="M2 2l9 9-9 9" fill="none" stroke="#fff" stroke-width="3"/></svg>
  </a>

  <a class="tile photo" role="img" aria-label="Circuit board and electronic components in teal light" style="background:radial-gradient(ellipse at 60% 35%,#5cc3cf 0%,#1f7a86 40%,#0b3a3e 90%)">
    <span class="label">Science &amp;<br>technology</span>
    <svg class="chev" viewBox="0 0 14 22"><path d="M2 2l9 9-9 9" fill="none" stroke="#fff" stroke-width="3"/></svg>
  </a>
  <a class="tile photo" role="img" aria-label="Engineer working on machinery in a workshop" style="background:radial-gradient(ellipse at 60% 35%,#9aabbf 0%,#4a6384 40%,#1a2a40 90%)">
    <span class="label">Mechanical<br>engineering</span>
    <svg class="chev" viewBox="0 0 14 22"><path d="M2 2l9 9-9 9" fill="none" stroke="#fff" stroke-width="3"/></svg>
  </a>
  <a class="tile tall photo" role="img" aria-label="Smartwatch with a digital clock face" style="background:radial-gradient(ellipse at 50% 45%,#6f7a86 0%,#3a434c 30%,#c3c9cf 60%,#e8eaec 100%)">
    <span class="label">Industrial design</span>
    <svg class="chev" viewBox="0 0 14 22"><path d="M2 2l9 9-9 9" fill="none" stroke="#fff" stroke-width="3"/></svg>
  </a>

  <a class="tile photo" role="img" aria-label="Business people discussing in a bright office" style="background:linear-gradient(135deg,#eef3f7,#a9bfd2 50%,#4d6a86)">
    <span class="label">Open innovation</span>
    <svg class="chev" viewBox="0 0 14 22"><path d="M2 2l9 9-9 9" fill="none" stroke="#fff" stroke-width="3"/></svg>
  </a>
  <a class="tile photo" role="img" aria-label="Electrical components under blue light" style="background:radial-gradient(ellipse at 55% 35%,#5ab4ea 0%,#0a6fb8 40%,#0a3b6e 90%)">
    <span class="label">Electrical<br>engineering</span>
    <svg class="chev" viewBox="0 0 14 22"><path d="M2 2l9 9-9 9" fill="none" stroke="#fff" stroke-width="3"/></svg>
  </a>

  <a class="tile wide photo" role="img" aria-label="Automated manufacturing production line" style="background:radial-gradient(ellipse at 35% 30%,#d6e5f1 0%,#7fa6c8 35%,#2e5580 70%,#1a3150 100%)">
    <span class="label">Manufacturing development</span>
    <svg class="chev" viewBox="0 0 14 22"><path d="M2 2l9 9-9 9" fill="none" stroke="#fff" stroke-width="3"/></svg>
  </a>
  <a class="tile photo" role="img" aria-label="Hands assembling a prototype device" style="background:radial-gradient(ellipse at 40% 30%,#e2e6ea 0%,#8a96a2 45%,#2b333c 95%)">
    <span class="label">Prototype<br>development</span>
    <svg class="chev" viewBox="0 0 14 22"><path d="M2 2l9 9-9 9" fill="none" stroke="#fff" stroke-width="3"/></svg>
  </a>
</main>

<footer class="site-footer">
  <div class="foot-col" style="left:88px">
    <h3>QUICK LINKS</h3>
    <ul><li>HOME</li><li>WORK</li><li>EXPERTISE</li><li>APPROACH</li><li>CLIENTS</li><li>ABOUT</li><li>CONTACT</li></ul>
  </div>
  <div class="foot-col" style="left:320px">
    <h3>EXPERTISE</h3>
    <ul><li>DESIGN</li><li>ENGINEERING</li><li>SOURCING</li><li>PRODUCTION</li><li>MANUFACTURING</li><li>INNOVATION</li></ul>
  </div>
  <div class="foot-col" style="left:572px">
    <h3>ABOUT</h3>
    <ul><li>ABOUT</li><li>HISTORY</li><li>CAREER</li><li>TEAM</li></ul>
  </div>
  <div class="foot-brand">
    <div class="brand-mark"></div>
    <div>
      <div class="brand-name">KELVARO</div>
      <div class="brand-tag">SUSTAINABLE SOLUTIONS</div>
    </div>
  </div>
  <div class="foot-phone">+45 61 87 34 09</div>
  <div class="social"><span></span><span></span><span></span><span></span></div>
  <div class="copyright">Copyright © 2015. All Rights Reserved</div>
</footer>
</body>
</html>
```